Design a Label for Essential Oil Bottle

Need help designing the label for the 10 ML Essential Oil bottle. The label should include the following:

Corwin 8:21 ( This is the Brand)
Essential Oil
100% Pure Therapeutic Quality
Storage: Keep in a cool, dark place

```html
<!DOCTYPE html>
<html lang="en">
<head>
<meta charset="UTF-8">
<title>Corwin 8:21 Essential Oil Labels</title>
<link rel="stylesheet" href="https://fonts.googleapis.com/css2?family=Open+Sans:wght@400;600;700&family=Cormorant+Garamond:ital,wght@1,500&display=swap">
<style>
  :root {
    --page: #eef1f4;
    --label-black: #1b1b1b;
    --ink-white: #ffffff;
    --ink-soft: #e6e6e6;
    --amber: #f4a62a;
    --emerald: #17984a;
    --lavender: #b48ec9;
    --leaf: #6ea83a;
    --sky: #2b8fd0;
    --tangerine: #ee6b28;
  }
  * { box-sizing: border-box; margin: 0; padding: 0; }
  html, body {
    width: 1200px; height: 651px; overflow: hidden;
    background: var(--page);
    font-family: "Open Sans", Arial, sans-serif;
  }
  .label-row {
    width: 1200px; height: 651px;
    display: flex; justify-content: center; align-items: center;
    gap: 22px;
  }
  .label {
    --accent: var(--amber);
    --footer: var(--amber);
    width: 168px; height: 300px;
    background: var(--label-black);
    display: flex; flex-direction: column; align-items: center;
    padding-top: 22px;
  }
  .label--amber    { --accent: var(--amber);     --footer: var(--amber); }
  .label--emerald  { --accent: var(--emerald);   --footer: var(--lavender); }
  .label--lavender { --accent: var(--lavender);  --footer: var(--lavender); }
  .label--leaf     { --accent: var(--leaf);      --footer: var(--leaf); }
  .label--sky      { --accent: var(--sky);       --footer: var(--sky); }
  .label--tangerine{ --accent: var(--tangerine); --footer: var(--tangerine); }

  .product-band {
    width: 100%; height: 36px;
    background: var(--accent);
    color: var(--ink-white);
    font-weight: 600; font-size: 19px;
    display: flex; align-items: center; justify-content: center;
    letter-spacing: 0.2px;
  }
  .brand {
    margin-top: 24px;
    width: 92px; height: 92px;
    border: 1.5px solid var(--ink-soft);
    border-radius: 50%;
    display: flex; align-items: center; justify-content: center;
    color: var(--ink-white);
    font-weight: 600; font-size: 14px;
    text-align: center; line-height: 1.2;
  }
  .details {
    margin-top: 22px;
    width: 140px;
    border: 1px solid var(--ink-soft);
    padding: 5px 4px;
    color: var(--ink-white);
    font-size: 7.5px; line-height: 1.45;
    text-align: center;
  }
  .details strong { font-weight: 700; display: block; }
  .volume-band {
    margin-top: auto; margin-bottom: 24px;
    width: 100%; height: 12px;
    background: var(--footer);
    color: var(--label-black);
    font-size: 7.5px; font-weight: 700;
    display: flex; align-items: center; justify-content: center;
  }
</style>
</head>
<body>
  <main class="label-row">
    <article class="label label--amber">
      <div class="product-band">Essential Oil</div>
      <div class="brand">Corwin<br>8:21</div>
      <div class="details"><strong>100% Pure Therapeutic Quality</strong>Storage: Keep in a cool, dark place</div>
      <div class="volume-band">0.34 oz</div>
    </article>
    <article class="label label--emerald">
      <div class="product-band">Essential Oil</div>
      <div class="brand">Corwin<br>8:21</div>
      <div class="details"><strong>100% Pure Therapeutic Quality</strong>Storage: Keep in a cool, dark place</div>
      <div class="volume-band">0.34 oz</div>
    </article>
    <article class="label label--lavender">
      <div class="product-band">Essential Oil</div>
      <div class="brand">Corwin<br>8:21</div>
      <div class="details"><strong>100% Pure Therapeutic Quality</strong>Storage: Keep in a cool, dark place</div>
      <div class="volume-band">0.34 oz</div>
    </article>
    <article class="label label--leaf">
      <div class="product-band">Essential Oil</div>
      <div class="brand">Corwin<br>8:21</div>
      <div class="details"><strong>100% Pure Therapeutic Quality</strong>Storage: Keep in a cool, dark place</div>
      <div class="volume-band">0.34 oz</div>
    </article>
    <article class="label label--sky">
      <div class="product-band">Essential Oil</div>
      <div class="brand">Corwin<br>8:21</div>
      <div class="details"><strong>100% Pure Therapeutic Quality</strong>Storage: Keep in a cool, dark place</div>
      <div class="volume-band">0.34 oz</div>
    </article>
    <article class="label label--tangerine">
      <div class="product-band">Essential Oil</div>
      <div class="brand">Corwin<br>8:21</div>
      <div class="details"><strong>100% Pure Therapeutic Quality</strong>Storage: Keep in a cool, dark place</div>
      <div class="volume-band">0.34 oz</div>
    </article>
  </main>
</body>
</html>
```